Business Card and Stationary for KVT Builders
Need standard business card, letterhead, and envelopes to incorporate our new logo
Business Card and Stationary for KVT Builders - Construction
Creative Brief
Simple
Rowan Pelley
Vice President
4621 Brantwell Houston, TX 77031
rowan@kvtbuilders.example
I'm open to layout ideas for all designs. letterhead and envelopes need to be accessible to incorporate microsoft office products.

```html
<!DOCTYPE html>
<html lang="en">
<head>
<meta charset="utf-8">
<title>KVT Builders — Stationery Set</title>
<link href="https://fonts.googleapis.com/css2?family=Roboto+Condensed:wght@700&family=Open+Sans:wght@400;600&display=swap" rel="stylesheet">
<style>
  :root{
    --bg:#e9e9ec;
    --paper:#ffffff;
    --brand:#4845c2;
    --brand-dark:#2d2c86;
    --grey:#85868c;
    --grey-light:#c9c9d0;
    --ink:#55565c;
    --faint:#e6e6f3;
    --shadow:0 2px 8px rgba(0,0,0,.18);
  }
  *{box-sizing:border-box;margin:0;padding:0}
  html,body{width:1200px;height:840px;overflow:hidden}
  body{background:var(--bg);font-family:"Open Sans",Arial,sans-serif;color:var(--ink);position:relative}

  .brand{font-family:"Roboto Condensed",Arial,sans-serif;font-weight:700;color:var(--brand-dark);white-space:nowrap;line-height:1}
  .brand-mark{display:inline-flex;align-items:center;gap:6px}
  .brand-mark .sq{display:inline-block;background:var(--brand)}
  .tagline{font-size:7px;font-weight:600;color:var(--brand-dark);letter-spacing:.02em;white-space:nowrap}

  /* envelopes */
  .envelope{position:absolute;left:40px;width:400px;height:170px;background:var(--paper);box-shadow:var(--shadow);overflow:hidden}
  .envelope svg{position:absolute;inset:0}
  .envelope .brand-mark{position:absolute;right:150px;top:22px}
  .envelope .brand{font-size:18px}
  .env-1{top:40px}
  .env-2{top:228px}
  .env-2 .brand,.env-3 .brand{color:var(--paper)}
  .env-2 .sq,.env-3 .sq{background:var(--paper)}
  .env-2 .brand-mark,.env-3 .brand-mark{top:auto;bottom:48px;right:150px}
  .env-3{top:416px}
  .env-front{top:610px;height:190px}
  .env-front .return{position:absolute;left:22px;top:22px}
  .env-front .return .brand{font-size:24px}
  .env-front .addr{font-size:7px;margin-top:4px}
  .env-front .ghost{position:absolute;right:24px;bottom:18px;font-size:46px;color:var(--faint)}

  /* letterhead */
  .letterhead{position:absolute;left:470px;top:50px;width:500px;height:707px;background:var(--paper);box-shadow:var(--shadow);padding:34px 44px}
  .lh-head{display:flex;justify-content:space-between;align-items:flex-start}
  .lh-head .brand{font-size:28px}
  .lh-head .tagline{font-size:9px;margin-top:4px}
  .lh-contact{font-size:7.5px;line-height:1.5;padding-top:4px;width:150px;white-space:nowrap}
  .lh-contact b{color:var(--brand-dark);display:inline-block;width:30px}
  .lh-body{margin-top:36px;font-size:8.5px;line-height:1.45}
  .lh-body p{margin-bottom:12px}
  .signature{width:70px;height:26px;background:linear-gradient(90deg,#d8d8de,#efeff3);margin:4px 0 4px}
  .lh-ghost{position:absolute;right:40px;bottom:34px;font-size:60px;color:var(--faint)}

  /* business cards */
  .card{position:absolute;left:1000px;width:170px;height:100px;background:var(--paper);box-shadow:var(--shadow);overflow:hidden}
  .card .brand-mark{position:absolute;left:50%;top:36px;transform:translateX(-50%)}
  .card .brand{font-size:17px}
  .card .url{position:absolute;left:14px;bottom:14px;font-size:6px;color:var(--grey)}
  .card-blue{background:var(--brand)}
  .card-grey{background:var(--grey)}
  .card-blue .brand,.card-grey .brand{color:var(--paper)}
  .card-blue .sq,.card-grey .sq{background:var(--paper)}
  .card-1{top:110px}.card-2{top:230px}.card-3{top:350px}.card-4{top:470px}
  .card-4 .front{position:absolute;left:10px;top:32px}
  .card-4 .brand{font-size:13px}
  .card-4 .tagline{font-size:4.2px;margin-top:2px}
  .card-4 .rule{position:absolute;left:84px;top:16px;bottom:16px;width:1px;background:var(--grey-light)}
  .card-4 .details{position:absolute;left:90px;top:18px;font-size:4.6px;line-height:1.65;white-space:nowrap}
  .card-4 .details .name{font-size:7.5px;font-weight:600;color:var(--brand-dark)}
  .card-4 .details .title{color:var(--brand)}
</style>
</head>
<body>

<section class="envelope env-1" aria-label="Envelope back, white">
  <svg viewBox="0 0 400 170" width="400" height="170" aria-hidden="true">
    <path d="M0 0 L400 0 L400 60 Q200 96 0 60 Z" fill="#f6f6f8"/>
  </svg>
  <div class="brand-mark"><span class="sq" style="width:10px;height:10px"></span><span class="brand">KVT Builders</span></div>
</section>

<section class="envelope env-2" aria-label="Envelope back, blue flap">
  <svg viewBox="0 0 400 170" width="400" height="170" aria-hidden="true">
    <path d="M0 70 Q200 20 400 70 L400 170 L0 170 Z" fill="var(--brand)"/>
  </svg>
  <div class="brand-mark"><span class="sq" style="width:10px;height:10px"></span><span class="brand">KVT Builders</span></div>
</section>

<section class="envelope env-3" aria-label="Envelope back, grey flap">
  <svg viewBox="0 0 400 170" width="400" height="170" aria-hidden="true">
    <path d="M0 70 Q200 20 400 70 L400 170 L0 170 Z" fill="var(--grey)"/>
  </svg>
  <div class="brand-mark"><span class="sq" style="width:10px;height:10px"></span><span class="brand">KVT Builders</span></div>
</section>

<section class="envelope env-front" aria-label="Envelope front">
  <div class="return">
    <div class="brand">KVT Builders</div>
    <div class="tagline">Commercial Concrete Contractors</div>
    <div class="addr">4621 Brantwell Houston, TX 77031</div>
  </div>
  <div class="brand ghost">KVT Builders</div>
</section>

<article class="letterhead">
  <header class="lh-head">
    <div>
      <div class="brand">KVT Builders</div>
      <div class="tagline">Commercial Concrete Contractors</div>
    </div>
    <div class="lh-contact">
      4621 Brantwell Houston, TX 77031<br>
      <b>Phone</b>(555) 014-2270<br>
      <b>Fax</b>(555) 014-2271
    </div>
  </header>
  <div class="lh-body">
    <p>Someone Some body<br>100 Harlow St<br>Brisbane, Australia</p>
    <p>Dear Someone Somebody,</p>
    <p>Lorem ipsum dolor sit amet, consectetuer adipiscing elit, sed diam nonummy nibh euismod tincidunt ut laoreet dolore magna aliquam erat volutpat. Ut wisi enim ad minim veniam, quis nostrud exerci tation ullamcorper suscipit lobortis nisl ut aliquip ex ea commodo consequat. Duis autem vel eum iriure dolor in hendrerit in vulputate velit esse molestie consequat, vel illum dolore eu feugiat nulla facilisis at vero eros et accumsan et iusto odio dignissim qui blandit praesent luptatum zzril delenit augue duis dolore te feugait nulla facilisi.</p>
    <p>Lorem ipsum dolor sit amet, consectetuer adipiscing elit, sed diam nonummy nibh euismod tincidunt ut laoreet dolore magna aliquam erat volutpat. Ut wisi enim ad minim veniam, quis nostrud exerci tation ullamcorper suscipit lobortis nisl ut aliquip ex ea commodo consequat. Duis autem vel eum iriure dolor in hendrerit in vulputate velit esse molestie consequat, vel illum dolore eu feugiat nulla facilisis at vero eros et accumsan et iusto odio dignissim qui blandit praesent luptatum zzril delenit augue duis dolore te feugait nulla facilisi.</p>
    <p>Lorem ipsum dolor sit amet, consectetuer adipiscing elit, sed diam nonummy nibh euismod tincidunt ut laoreet dolore magna aliquam erat volutpat. Ut wisi enim ad minim veniam, quis nostrud exerci tation ullamcorper suscipit lobortis nisl ut aliquip ex ea commodo consequat. Duis autem vel eum iriure dolor in hendrerit in vulputate velit esse molestie consequat, vel illum dolore eu feugiat nulla facilisis at vero eros et accumsan et iusto odio dignissim qui blandit praesent luptatum zzril delenit augue duis dolore te feugait nulla facilisi.</p>
    <p>Your Sincerely,<br>Elise Marlow</p>
    <div class="signature" role="img" aria-label="Handwritten signature"></div>
  </div>
  <div class="brand lh-ghost">KVT Builders</div>
</article>

<section class="card card-1" aria-label="Business card front, white">
  <div class="brand-mark"><span class="sq" style="width:8px;height:8px"></span><span class="brand">KVT Builders</span></div>
  <div class="url">www.kvtbuilders.example</div>
</section>

<section class="card card-2 card-blue" aria-label="Business card front, blue">
  <div class="brand-mark"><span class="sq" style="width:8px;height:8px"></span><span class="brand">KVT Builders</span></div>
</section>

<section class="card card-3 card-grey" aria-label="Business card front, grey">
  <div class="brand-mark"><span class="sq" style="width:8px;height:8px"></span><span class="brand">KVT Builders</span></div>
</section>

<section class="card card-4" aria-label="Business card back with contact details">
  <div class="front">
    <div class="brand">KVT Builders</div>
    <div class="tagline">Commercial Concrete Contractors</div>
  </div>
  <div class="rule"></div>
  <div class="details">
    <div class="name">Rowan Pelley</div>
    <div class="title">Vice President</div>
    <div>4621 Brantwell</div>
    <div>Houston, TX 77031</div>
    <div>P (555) 014-2270</div>
    <div>F (555) 014-2271</div>
    <div>rowan@kvtbuilders.example</div>
    <div>kvtbuilders.example</div>
  </div>
</section>

</body>
</html>
```